Nine nights under a pale lamp - II

Cover for the book "Nine nights under the pale lamp".
Author: "Maribel Toquet"
Publisher: "Editions Corvane" (at the bottom of the page)
Book 14 x 20.5 cm

In the previous project ("9 nights under a pale lamp"), I proposed a photo of a woman with silvery hair.
I think I made a mistake that forced the artists in a direction and limited the creativity.

Therefore, I now offer only key-words:
A mature woman, still beautiful and dressed like a young one, also sensual and radiant.
She is on vacation by the seaside.

Please note that the cover is in French:
Maribel Toquet
Nine nights under a pale lamp
Corvane Editions

Adults, all ages, often women

book

• elegance, maybe a bit of snobbery

```html
<!DOCTYPE html>
<html lang="fr">
<head>
<meta charset="utf-8">
<title>Neuf nuits sous la lampe pâle — Maribel Toquet</title>
<link rel="stylesheet" href="https://fonts.googleapis.com/css2?family=Antonio:wght@200;300&display=swap">
<style>
  :root {
    --page-bg: #e9e6e2;
    --ink-dark: #4a4a4c;
    --ink-accent: #ef5d72;
    --sky-top: #f4f8fb;
    --sky-mid: #cfe6f2;
    --sea: #5fd0d8;
    --sea-light: #a9e3e6;
    --sand: #efe4d6;
    --skin-warm: #c98c6a;
  }
  * { margin: 0; padding: 0; box-sizing: border-box; }
  html, body {
    width: 1200px;
    height: 1000px;
    overflow: hidden;
    background: var(--page-bg);
  }
  .book-cover {
    position: absolute;
    left: 258px;
    top: 0;
    width: 684px;
    height: 1000px;
    overflow: hidden;
    font-family: "Antonio", "Arial Narrow", sans-serif;
  }
  .cover-photo {
    position: absolute;
    inset: 0;
    background:
      radial-gradient(ellipse 48% 62% at 76% 58%, rgba(214,168,132,0.85), rgba(214,168,132,0) 70%),
      linear-gradient(180deg,
        var(--sky-top) 0%,
        var(--sky-mid) 22%,
        #e6f1f6 27%,
        var(--sea) 29%,
        var(--sea-light) 45%,
        #dff1f0 62%,
        var(--sand) 82%,
        #d9cfc4 100%);
  }
  .author-name,
  .title-line,
  .publisher-name {
    position: absolute;
    left: 68px;
    white-space: nowrap;
    line-height: 1;
    text-transform: uppercase;
  }
  .author-name {
    top: 178px;
    font-size: 55px;
    font-weight: 300;
    letter-spacing: 2px;
    color: var(--ink-dark);
  }
  .title-line {
    font-size: 118px;
    font-weight: 200;
    letter-spacing: 1px;
  }
  .title-line--dark { color: var(--ink-dark); }
  .title-line--accent { color: var(--ink-accent); }
  .title-line:nth-child(1) { top: 292px; }
  .title-line:nth-child(2) { top: 426px; }
  .title-line:nth-child(3) { top: 556px; }
  .title-line:nth-child(4) { top: 688px; }
  .book-title { position: absolute; inset: 0; }
  .publisher-name {
    left: 75px;
    top: 944px;
    font-size: 25px;
    font-weight: 300;
    letter-spacing: 2.5px;
    color: var(--ink-dark);
  }
</style>
</head>
<body>
  <main class="book-cover">
    <div class="cover-photo" role="img" aria-label="Photographie : une femme blonde en lunettes de soleil et tunique en crochet, assise de dos au bord de la mer turquoise, sous un ciel lumineux"></div>
    <p class="author-name">Maribel Toquet</p>
    <h1 class="book-title">
      <span class="title-line title-line--dark">Neuf nuits</span>
      <span class="title-line title-line--accent">sous la</span>
      <span class="title-line title-line--dark">lampe</span>
      <span class="title-line title-line--accent">pâle</span>
    </h1>
    <p class="publisher-name">Editions Corvane</p>
  </main>
</body>
</html>
```